Web design for a Crane & Heavy Equipment Inspection, Repair and Maintenance Company in Texas

We need a web design for a new company based in Houston, Texas called "Bristen Hoist & Equipment". We inspect, repair and maintain diesel driven heavy equipment, generators, fire water pumps and cranes. We would like to see designs that use the colors orange, white, yellow and brown, and/or orange, white, navy, yellow and grey.

```html
<!DOCTYPE html>
<html lang="en">
<head>
<meta charset="utf-8">
<title>Bristen Hoist &amp; Equipment</title>
<link rel="stylesheet" href="https://fonts.googleapis.com/css2?family=Orbitron:wght@600;700;800&family=Open+Sans:wght@400;600;700&display=swap">
<style>
  :root{
    --orange:#e8532a;
    --navy:#1d4f86;
    --brown:#7d2a14;
    --text:#8a8a8a;
    --nav:#6b6b6b;
    --rule:#e2e2e2;
    --footer:#2b2b2b;
    --footer-text:#bdbdbd;
  }
  *{margin:0;padding:0;box-sizing:border-box}
  html,body{width:1022px;height:1200px;overflow:hidden;background:#fff}
  body{position:relative;font-family:"Open Sans",Arial,sans-serif;color:var(--text)}

  .site-header{position:absolute;left:0;top:0;width:1022px;height:118px}
  .brand{position:absolute;left:86px;top:40px;font-family:"Orbitron",sans-serif;font-weight:800;font-size:22px;line-height:24px;color:var(--navy);letter-spacing:.5px}
  .brand small{display:block;font-size:14px;letter-spacing:1px}
  .service-line{position:absolute;right:85px;top:26px;font-size:12px;color:#9a9a9a}
  .service-line strong{color:var(--orange);font-size:17px;font-weight:600}
  .main-nav{position:absolute;right:85px;top:78px;display:flex;gap:28px;font-family:"Orbitron",sans-serif;font-weight:600;font-size:13px;letter-spacing:.6px}
  .main-nav a{color:var(--nav);text-decoration:none}
  .main-nav a.active{color:var(--navy);font-weight:700}

  .hero{position:absolute;left:0;top:118px;width:1022px;height:436px;
    background:linear-gradient(180deg,#5f8f99 0%,#9cc1bd 22%,#d9b8c2 42%,#eed08a 62%,#f3c21e 78%,#c98a12 88%,#1e1a14 96%,#111 100%)}
  .hero-title{position:absolute;left:86px;top:120px;font-family:"Orbitron",sans-serif;font-weight:700;font-size:22px;line-height:25px;color:#fff;letter-spacing:.8px}
  .hero-arrow{position:absolute;top:203px;width:29px;height:29px;border-radius:50%;background:rgba(255,255,255,.8)}
  .hero-arrow.prev{left:18px}.hero-arrow.next{right:18px}
  .hero-arrow svg{display:block}

  .welcome{position:absolute;left:0;top:590px;width:1022px;text-align:center}
  .section-title{font-family:"Orbitron",sans-serif;font-weight:700;color:var(--brown);font-size:19px;letter-spacing:1px}
  .welcome p{width:790px;margin:10px auto 0;font-size:13px;line-height:23px}

  .rule{position:absolute;left:86px;width:852px;height:1px;background:var(--rule)}

  .services{position:absolute;left:86px;top:768px;width:852px;display:flex;justify-content:space-between}
  .service{width:270px;text-align:center}
  .service svg{display:block;margin:0 auto;height:60px}
  .service h3{font-family:"Orbitron",sans-serif;font-weight:700;color:var(--brown);font-size:16px;letter-spacing:.8px;margin-top:20px}
  .service p{font-size:12px;line-height:18px;margin-top:12px}

  .clients{position:absolute;left:86px;top:986px;width:852px;text-align:center}
  .clients h4{font-weight:400;font-size:13px;color:#444}
  .client-row{display:flex;justify-content:space-between;align-items:center;margin-top:14px;padding:0 12px}
  .client-row span{font-weight:600;font-size:17px;color:#8e8e8e}

  .site-footer{position:absolute;left:0;top:1076px;width:1022px;height:124px;background:linear-gradient(#333,#232323)}
  .footer-nav{position:absolute;left:230px;top:22px;display:flex;gap:0;font-size:12px}
  .footer-nav a{color:var(--footer-text);text-decoration:none}
  .footer-nav a::before{content:"• ";font-size:9px}
  .footer-rule{position:absolute;left:86px;top:59px;width:852px;height:1px;background:#444}
  .copyright{position:absolute;left:86px;top:82px;font-size:12px;color:var(--footer-text)}
  .social{position:absolute;left:870px;top:78px;display:flex;gap:12px}
  .social span{width:26px;height:26px;border-radius:50%}
  .social .fanlink{background:#3b5998}.social .chirpnet{background:#2aa9e0}
</style>
</head>
<body>
<header class="site-header">
  <div class="brand">BRISTEN HOIST<small>&amp; EQUIPMENT</small></div>
  <div class="service-line">For Service &amp; Inspections <strong>Call : 555.014.2290</strong></div>
  <nav class="main-nav">
    <a class="active" href="#">HOME</a><a href="#">ABOUT US</a><a href="#">SERVICES</a><a href="#">CAREER</a><a href="#">CONTACT US</a>
  </nav>
</header>

<section class="hero" role="img" aria-label="Tower crane silhouette against a sunset sky">
  <h2 class="hero-title">MAECENAS RUTRUM<br>ERAT TURPIS</h2>
  <span class="hero-arrow prev"><svg width="29" height="29"><path d="M16 9l-5 5.5 5 5.5" fill="none" stroke="#888" stroke-width="1.5"/></svg></span>
  <span class="hero-arrow next"><svg width="29" height="29"><path d="M13 9l5 5.5-5 5.5" fill="none" stroke="#888" stroke-width="1.5"/></svg></span>
</section>

<section class="welcome">
  <h2 class="section-title">WELCOME TO BRISTEN HOIST</h2>
  <p>Bristen Hoist and Equipment Services Company, LLC provides on-site crane, generator and heavy equipment repair, maintenance and inspection. Our commitment to our clients extends beyond our core values of safety, honesty, quality and reliability. We are leveraging technology to improve our clients’ access to inspection, maintenance and repair records.</p>
</section>

<div class="rule" style="top:729px"></div>

<section class="services">
  <article class="service">
    <svg viewBox="0 0 60 60" fill="none" stroke="#7d2a14" stroke-width="2"><rect x="10" y="5" width="40" height="52"/><rect x="14" y="9" width="32" height="44"/><rect x="22" y="1" width="16" height="8"/><path d="M19 20h22M19 27h22M19 34h22M19 41h22M19 47h14"/></svg>
    <h3>INSPECTIONS</h3>
    <p>Proin eget elit nisi. Proin id velit placerat, viverra nunc quis, facilisis erat. Etiam vestibulum, enim eu scelerisque finibus, dui mauris.</p>
  </article>
  <article class="service">
    <svg viewBox="0 0 60 60" fill="none" stroke="#7d2a14" stroke-width="2"><path d="M6 4l4 4 30 38 8 8 4-4-8-8L10 8z"/><path d="M48 6a10 10 0 0 0-11 14L8 48a4 4 0 0 0 6 6l28-29a10 10 0 0 0 14-11l-6 6-6-2-2-6z"/></svg>
    <h3>REPAIRS</h3>
    <p>Proin eget elit nisi. Proin id velit placerat, viverra nunc quis, facilisis erat. Etiam vestibulum, enim eu scelerisque finibus, dui mauris.</p>
  </article>
  <article class="service">
    <svg viewBox="0 0 76 60" fill="none" stroke="#7d2a14" stroke-width="2"><circle cx="24" cy="36" r="14" stroke-dasharray="6 3"/><circle cx="24" cy="36" r="10"/><circle cx="24" cy="36" r="5"/><circle cx="56" cy="16" r="11" stroke-dasharray="5 3"/><circle cx="56" cy="16" r="7"/><circle cx="56" cy="16" r="3"/></svg>
    <h3>MAINTENANCE</h3>
    <p>Proin eget elit nisi. Proin id velit placerat, viverra nunc quis, facilisis erat. Etiam vestibulum, enim eu scelerisque finibus, dui mauris.</p>
  </article>
</section>

<div class="rule" style="top:968px"></div>

<section class="clients">
  <h4>Clients</h4>
  <div class="client-row">
    <span>Larkmoor</span><span>Quorra</span><span>Netvale</span><span>Sorrel</span><span>Kitamo</span><span>Brightel</span><span>Mistrale</span><span>Arvento</span><span>Cindra</span>
  </div>
</section>

<footer class="site-footer">
  <nav class="footer-nav">
    <a href="#" style="width:96px">Home</a><a href="#" style="width:136px">About us</a><a href="#" style="width:132px">Services</a><a href="#" style="width:129px">Careers</a><a href="#">Contact us</a>
  </nav>
  <div class="footer-rule"></div>
  <p class="copyright">Copyright © 2014 Bristen Hoist &amp; Equipment. All rights reserved.</p>
  <div class="social">
    <span class="fanlink" role="img" aria-label="Fanlink"></span>
    <span class="chirpnet" role="img" aria-label="Chirpnet"></span>
  </div>
</footer>
</body>
</html>
```